Logo for Brisk Partners LLC needs a design

This logo will be for a food handler and restaurant manager training business located. I am a registered trainer and proctor for KitchGuard, the Federal Dining League. colors options should be black, white, blue, silver or something else bold. The file that I have sent needs to be on the card somewhere, small.
Updates

need to have the KitchGuard logo that I added on the card. BRISK stands for basic regulated instruction for service kitchens.

Logo Text

Dennis JonesStar ,Associates LLC. , Registered trainer and proctorwith KitchGuard.

```html
<!DOCTYPE html>
<html lang="en">
<head>
<meta charset="utf-8">
<title>Brisk Partners LLC — Business Card</title>
<link href="https://fonts.googleapis.com/css2?family=Poppins:wght@400;500;700&display=swap" rel="stylesheet">
<style>
  :root {
    --navy: #253c87;
    --white: #ffffff;
    --ink: #111111;
    --sky: #2a9bd8;
    --lavender: #b08bd6;
    --stage: #e9eaee;
  }
  * { margin: 0; padding: 0; box-sizing: border-box; }
  html, body { width: 1200px; height: 1108px; overflow: hidden; }
  body {
    background: var(--stage);
    font-family: "Poppins", sans-serif;
    position: relative;
  }
  .card {
    position: absolute;
    top: 116px;
    width: 500px;
    height: 875px;
    border-radius: 22px;
    overflow: hidden;
    box-shadow: 0 10px 30px rgba(0,0,0,.18);
  }
  .card--back { left: 70px; background: var(--navy); }
  .card--front { left: 630px; background: var(--white); }

  .brand {
    position: absolute;
    left: 0; right: 0;
    display: flex;
    align-items: center;
    justify-content: center;
    gap: 14px;
    font-weight: 700;
    line-height: 1;
  }
  .brand__dot { width: 22px; height: 22px; border-radius: 50%; background: currentColor; }
  .brand__text { display: flex; flex-direction: column; align-items: flex-start; }
  .brand__name { font-size: 62px; letter-spacing: 1px; }
  .brand__sub { font-size: 17px; letter-spacing: 1.5px; margin-top: 6px; }
  .card--back .brand { top: 380px; color: var(--white); }
  .card--front .brand { top: 110px; color: var(--ink); }

  .front-bg { position: absolute; inset: 0; }

  .details {
    position: absolute;
    top: 320px; left: 0; right: 0;
    text-align: center;
    color: var(--white);
  }
  .details__name { font-size: 34px; font-weight: 500; letter-spacing: .5px; }
  .details__title { font-size: 17px; font-weight: 400; margin-top: 2px; }
  .divider { width: 16px; height: 2px; background: var(--lavender); margin: 12px auto; }
  .icons { display: flex; justify-content: center; gap: 14px; margin-bottom: 8px; }
  .icons svg { width: 14px; height: 14px; }
  .details__line { font-size: 19px; font-weight: 400; line-height: 1.45; }
  .details__address { margin-top: 4px; }

  .cert {
    position: absolute;
    bottom: 40px; left: 0; right: 0;
    display: flex; flex-direction: column; align-items: center;
  }
  .cert__badge { width: 120px; height: 40px; border-radius: 20px; background: #cfe3f4; border: 2px solid var(--sky); }
  .cert__caption {
    margin-top: 8px;
    font-family: "Poppins", sans-serif;
    font-size: 11px; line-height: 1.3; text-align: center; color: #333;
  }
</style>
</head>
<body>
  <section class="card card--back" aria-label="Card back">
    <div class="brand">
      <span class="brand__dot"></span>
      <div class="brand__text">
        <span class="brand__name">BRISK</span>
        <span class="brand__sub">PARTNERS LLC</span>
      </div>
    </div>
  </section>

  <section class="card card--front" aria-label="Card front">
    <svg class="front-bg" viewBox="0 0 500 875" preserveAspectRatio="none" aria-hidden="true">
      <path d="M0,300 Q250,200 500,300 L500,720 Q250,690 0,840 Z" fill="#253c87"/>
    </svg>

    <div class="brand">
      <span class="brand__dot"></span>
      <div class="brand__text">
        <span class="brand__name">BRISK</span>
        <span class="brand__sub">PARTNERS LLC</span>
      </div>
    </div>

    <div class="details">
      <p class="details__name">MARVIN PELT</p>
      <p class="details__title">YOUR TITLE HERE</p>
      <div class="divider"></div>
      <div class="icons">
        <svg viewBox="0 0 24 24" fill="#fff"><path d="M6.6 10.8a15 15 0 006.6 6.6l2.2-2.2c.3-.3.7-.4 1-.2 1.1.4 2.3.6 3.6.6.6 0 1 .4 1 1V20c0 .6-.4 1-1 1A17 17 0 013 4c0-.6.4-1 1-1h3.5c.6 0 1 .4 1 1 0 1.3.2 2.5.6 3.6.1.3 0 .7-.2 1z"/></svg>
        <svg viewBox="0 0 24 24" fill="#fff"><path d="M3 5h18v14H3z"/><path d="M3 5l9 7 9-7" fill="none" stroke="#253c87" stroke-width="2"/></svg>
        <svg viewBox="0 0 24 24" fill="none" stroke="#fff" stroke-width="2"><circle cx="12" cy="12" r="9"/><path d="M3 12h18M12 3c3 3 3 15 0 18M12 3c-3 3-3 15 0 18"/></svg>
      </div>
      <p class="details__line">312 555 0187</p>
      <p class="details__line">marvin@briskpartners.com</p>
      <p class="details__line">www.briskpartners.com</p>
      <div class="divider"></div>
      <p class="details__line details__address">418 Alder Street NE<br>Suite 210, Lakemont<br>MI 49620</p>
    </div>

    <div class="cert">
      <div class="cert__badge"></div>
      <p class="cert__caption">Registered KitchGuard Proctor<br>&amp; Certified KitchGuard Instructor</p>
    </div>
  </section>
</body>
</html>
```